Flyer Design Project for lawn care business

I need a flyer designed for my lawn care business, "Ashby's Groundcare Services".  It is a family owned small landscaping company. I was thinking something that I can print  2- 3 per page.
I have  2 different logos I can upload to give an idea.  I have seen some I like that are colorfull with neat graphics but I also like some that are simple and elegant.  I would like something that catches your eye and looks professionaly done.

Target Market(s)
Homeowners in Durham, North Carolina with homes usually valued $200,000 or more.
Industry/Entity Type
Landscaping
Requirements
Must have
- I would like the address of my website listed on it, www.ashbygroundcareservices.com
I would like for it to say somewhere, 50% off first service with seasonal service.
Not sure if I want to list some of the services that I offer or just say full service lawn care.
Nice to have
- I have a logo with a bull pushing a lawn mower.  I live in Durham, NC also known as the Bull City.  I am not in love with the logo so feel free to change it or not use it at all.

```html
<!DOCTYPE html>
<html lang="en">
<head>
<meta charset="UTF-8">
<title>Ashby's Groundcare Services – Flyer</title>
<link href="https://fonts.googleapis.com/css2?family=Fira+Sans+Condensed:ital,wght@0,600;1,400;1,600&display=swap" rel="stylesheet">
<style>
  :root {
    --ink: #000000;
    --paper: #ffffff;
    --sheet: #f7f5f6;
    --grass-light: #b9dc8f;
    --grass: #7cc04a;
    --grass-deep: #4f9a2c;
    --divider: #111111;
    --brand: #1c1c1c;
  }
  * { box-sizing: border-box; margin: 0; padding: 0; }
  html, body { width: 887px; height: 1200px; overflow: hidden; background: var(--paper); }
  body { font-family: "Fira Sans Condensed", "Arial Narrow", sans-serif; }

  .sheet {
    width: 887px; height: 1200px;
    display: flex; flex-direction: column;
    gap: 4px; background: var(--divider);
  }
  .flyer {
    position: relative; flex: 1; overflow: hidden;
    background: var(--sheet);
  }
  .flyer__grass {
    position: absolute; inset: 0;
    background: linear-gradient(to bottom,
      var(--sheet) 0%,
      rgba(185,220,143,0.55) 22%,
      var(--grass-light) 55%,
      var(--grass) 85%,
      var(--grass-deep) 100%);
  }
  .flyer__title {
    position: absolute; left: 148px; top: 6px;
    font-size: 47px; font-style: italic; font-weight: 600;
    letter-spacing: -1.5px; color: var(--paper);
    text-shadow: 0 0 2px var(--ink), 2px 2px 0 var(--ink), -2px -2px 0 var(--ink),
                 2px -2px 0 var(--ink), -2px 2px 0 var(--ink), 3px 3px 2px var(--ink);
  }
  .flyer__tagline {
    position: absolute; right: 84px; top: 64px;
    font-size: 45px; font-style: italic; font-weight: 400;
    letter-spacing: -0.5px; color: var(--ink);
    text-shadow: 0 0 3px var(--paper), 0 0 3px var(--paper);
  }
  .brand {
    position: absolute; left: 26px; top: 125px; width: 340px;
    text-align: center; color: var(--brand);
    font-size: 44px; font-weight: 600; line-height: 1.05;
  }
  .flyer__phone {
    position: absolute; left: 410px; top: 168px;
    font-size: 70px; font-style: italic; font-weight: 600;
    letter-spacing: -3px; color: var(--paper);
    text-shadow: 0 0 2px var(--ink), 3px 3px 0 var(--ink), -3px -3px 0 var(--ink),
                 3px -3px 0 var(--ink), -3px 3px 0 var(--ink), 4px 4px 3px var(--ink);
  }
  .flyer__web {
    position: absolute; right: 12px; top: 294px;
    font-size: 32px; font-style: italic; font-weight: 400;
    letter-spacing: -0.6px; color: var(--ink);
    text-shadow: 1px 1px 0 var(--paper), -1px -1px 0 var(--paper),
                 1px -1px 0 var(--paper), -1px 1px 0 var(--paper), 0 0 3px var(--paper);
  }
  .flyer__offer {
    position: absolute; left: 82px; top: 330px;
    font-size: 38px; font-style: italic; font-weight: 400;
    letter-spacing: -1.2px; color: var(--ink);
    text-shadow: 2px 2px 0 var(--paper), -2px -2px 0 var(--paper),
                 2px -2px 0 var(--paper), -2px 2px 0 var(--paper), 0 0 3px var(--paper);
  }
</style>
</head>
<body>
<main class="sheet">
  <section class="flyer">
    <div class="flyer__grass" role="img" aria-label="Tall green grass blades rising from the bottom"></div>
    <h1 class="flyer__title">Ashby's Groundcare Services</h1>
    <p class="flyer__tagline">full service lawn care</p>
    <div class="brand">Ashby's<br>Lawn Care</div>
    <p class="flyer__phone">(919)-555-0142</p>
    <p class="flyer__web">www.ashbygroundcareservices.com</p>
    <p class="flyer__offer">50% off first service with seasonal service!!</p>
  </section>
  <section class="flyer">
    <div class="flyer__grass" role="img" aria-label="Tall green grass blades rising from the bottom"></div>
    <h1 class="flyer__title">Ashby's Groundcare Services</h1>
    <p class="flyer__tagline">full service lawn care</p>
    <div class="brand">Ashby's<br>Lawn Care</div>
    <p class="flyer__phone">(919)-555-0142</p>
    <p class="flyer__web">www.ashbygroundcareservices.com</p>
    <p class="flyer__offer">50% off first service with seasonal service!!</p>
  </section>
  <section class="flyer">
    <div class="flyer__grass" role="img" aria-label="Tall green grass blades rising from the bottom"></div>
    <h1 class="flyer__title">Ashby's Groundcare Services</h1>
    <p class="flyer__tagline">full service lawn care</p>
    <div class="brand">Ashby's<br>Lawn Care</div>
    <p class="flyer__phone">(919)-555-0142</p>
    <p class="flyer__web">www.ashbygroundcareservices.com</p>
    <p class="flyer__offer">50% off first service with seasonal service!!</p>
  </section>
</main>
</body>
</html>
```